Architecture firm needing a business card

We need a business card design for a new company based in the US called "Pellmore Architecture". Seeking minimalist designs that have a creativity/design feel but must be clean and professional. Please refer to the logo attached.

Target Market(s)

Real Estate Investors, Home Builders and Construction Firms.

Industry/Entity Type

Architecture

Contact Information for Business Card

Standard US size business cards. Would like to have some sort of graphic on the back side of the card - nothing that is too loud but something that may catch your attention. More or less grayscale colors that are in line with the logo colors (navy and greys essentially). Additional colors maybe accepted if blended properly (earthtones), but might be difficult to accomplish and maintain the clean/minimalist look.

Requirements
Must have
• Clean Lines
Nice to have
• some sort of graphics, would like to have something creative on the back side of the card
Should not have
• nothing too busy, cluttered or overwhelming.

```html
<!DOCTYPE html>
<html lang="en">
<head>
<meta charset="utf-8">
<title>Pellmore Architecture — Business Card</title>
<link rel="stylesheet" href="https://fonts.googleapis.com/css2?family=Open+Sans:wght@300;400;600&display=swap">
<style>
  :root {
    --navy: #1d4a8f;
    --navy-deep: #143a78;
    --navy-light: #2c5ea8;
    --ink: #3a3f47;
    --grey: #8a9099;
    --paper: #ffffff;
    --backdrop: #e9ebee;
  }
  * { box-sizing: border-box; margin: 0; padding: 0; }
  html, body { width: 1200px; height: 749px; overflow: hidden; }
  body {
    background: var(--backdrop);
    font-family: "Open Sans", sans-serif;
    position: relative;
  }
  .card {
    position: absolute;
    top: 226px;
    width: 520px;
    height: 297px;
    overflow: hidden;
    box-shadow: 0 2px 10px rgba(0,0,0,0.12);
  }
  .card-front { left: 50px; background: var(--paper); }
  .card-back { left: 630px; }

  .wordmark { display: flex; align-items: center; gap: 8px; }
  .wordmark-square { width: 14px; height: 14px; background: var(--navy); }
  .wordmark-name {
    font-weight: 300; font-size: 22px; letter-spacing: 1px;
    line-height: 1; color: var(--navy); text-transform: uppercase;
  }
  .wordmark-sub {
    display: block; font-size: 8px; letter-spacing: 3px; margin-top: 3px;
  }
  .card-front .wordmark { position: absolute; left: 34px; top: 36px; }

  .person { position: absolute; left: 62px; top: 112px; }
  .person-name { font-size: 21px; font-weight: 400; color: var(--navy); }
  .person-role { font-size: 9px; color: var(--grey); margin-top: 1px; }

  .address { position: absolute; left: 62px; top: 178px; font-size: 7.5px; line-height: 1.45; color: var(--grey); }
  .address-firm { font-size: 8.5px; font-weight: 600; color: var(--navy); margin-bottom: 3px; }

  .contact { position: absolute; right: 30px; top: 196px; list-style: none; font-size: 7.5px; color: var(--ink); }
  .contact li { display: flex; align-items: center; gap: 6px; line-height: 1.7; }
  .contact svg { width: 8px; height: 8px; fill: var(--navy); }

  .edge-band {
    position: absolute; left: 0; right: 0; bottom: 0; height: 7px;
    background: linear-gradient(90deg, var(--navy-deep), var(--navy-light) 60%, #5d8ed0);
  }

  .back-pattern {
    position: absolute; inset: 0;
    background: radial-gradient(ellipse at 35% 30%, var(--navy-light), var(--navy) 50%, var(--navy-deep));
  }
  .card-back .wordmark { position: absolute; left: 50%; top: 118px; transform: translateX(-50%); }
  .card-back .wordmark-square { background: #ffffff; }
  .card-back .wordmark-name { color: #ffffff; }
  .back-web {
    position: absolute; left: 0; right: 0; top: 176px; text-align: center;
    font-size: 9px; letter-spacing: 6px; color: rgba(255,255,255,0.75);
  }
</style>
</head>
<body>
  <section class="card card-front">
    <div class="wordmark">
      <span class="wordmark-square"></span>
      <span class="wordmark-name">Pellmore<span class="wordmark-sub">Architecture</span></span>
    </div>
    <div class="person">
      <p class="person-name">Lorem ipsum</p>
      <p class="person-role">Managing Director</p>
    </div>
    <div class="address">
      <p class="address-firm">Pellmore Architecture</p>
      <p>1820 Harbor Lane, Suite 4</p>
      <p>Portland, Oregon 97201</p>
      <p>United States</p>
      <p>555 014 2278</p>
    </div>
    <ul class="contact">
      <li><svg viewBox="0 0 10 10"><path d="M2 0h2l1 3-1.5 1a6 6 0 0 0 2.5 2.5L7 5l3 1v2c0 1-1 2-2 2A8 8 0 0 1 0 2c0-1 1-2 2-2z"/></svg>+1 555 014 2278</li>
      <li><svg viewBox="0 0 10 10"><path d="M0 2h10v6H0z M0 2l5 3.5L10 2" /></svg>info@pellmore.com</li>
      <li><svg viewBox="0 0 10 10"><circle cx="5" cy="5" r="5"/></svg>www.pellmore.com</li>
    </ul>
    <div class="edge-band"></div>
  </section>

  <section class="card card-back">
    <div class="back-pattern" role="img" aria-label="Navy low-poly faceted geometric pattern"></div>
    <div class="wordmark">
      <span class="wordmark-square"></span>
      <span class="wordmark-name">Pellmore<span class="wordmark-sub">Architecture</span></span>
    </div>
    <p class="back-web">www.pellmore.com</p>
  </section>
</body>
</html>
```